PowerPoint Template

We would like new powerpoint template for our organization: Fjordline Data Guild.
Enclosed you find our logo and old template.
Industry/Entity Type
Computer
Requirements
Must have
- 1. Logo
2. Footer (for autor)
3. Font: Variations of ARIAL

```html
<!DOCTYPE html>
<html lang="en">
<head>
<meta charset="utf-8">
<title>New Product Development 2014 – Fjordline Data Guild</title>
<link rel="stylesheet" href="https://fonts.googleapis.com/css2?family=Arimo:wght@400;700&display=swap">
<style>
  :root {
    --stage-light: #f2f2f2;
    --stage-mid: #c9c9c9;
    --slide-dark: #262626;
    --slide-mid: #5a5a5a;
    --slide-glow: #d9d9d9;
    --footer-band: #2a2a2a;
    --ribbon-light: #fbf2d0;
    --ribbon-deep: #f1dd9f;
    --ribbon-ink: #1c1c1c;
    --mark-red: #e8394a;
    --text-light: #ffffff;
    --text-soft: #f0f0f0;
  }
  html, body {
    margin: 0;
    padding: 0;
    width: 1200px;
    height: 1000px;
    overflow: hidden;
  }
  body {
    background: radial-gradient(ellipse at 50% 0%, var(--stage-mid) 0%, #bdbdbd 45%, var(--stage-light) 100%);
    font-family: "Arimo", Arial, sans-serif;
    position: relative;
  }
  .slide {
    position: absolute;
    left: 84px;
    top: 93px;
    width: 1056px;
    height: 792px;
    overflow: hidden;
    background:
      radial-gradient(ellipse 560px 500px at 910px 240px, var(--slide-glow) 0%, #a3a3a3 28%, var(--slide-mid) 58%, rgba(58,58,58,0) 100%),
      linear-gradient(180deg, var(--slide-dark) 0%, #3c3c3c 40%, #4d4d4d 100%);
  }
  .ribbon {
    position: absolute;
    left: 63px;
    top: 0;
    width: 206px;
    height: 309px;
    filter: drop-shadow(4px 8px 8px rgba(0,0,0,0.45));
  }
  .ribbon__shape { position: absolute; inset: 0; }
  .ribbon__url {
    position: absolute;
    top: 44px;
    left: 0;
    width: 206px;
    text-align: center;
    font-weight: 700;
    font-size: 19px;
    color: var(--ribbon-ink);
  }
  .ribbon__brand {
    position: absolute;
    top: 112px;
    left: 18px;
    width: 170px;
    display: flex;
    align-items: center;
    gap: 10px;
  }
  .ribbon__square {
    flex: none;
    width: 22px;
    height: 22px;
    background: var(--mark-red);
  }
  .ribbon__name {
    font-weight: 700;
    font-size: 24px;
    line-height: 1.15;
    color: var(--ribbon-ink);
  }
  .content {
    position: absolute;
    left: 446px;
    top: 165px;
    width: 540px;
    color: var(--text-light);
  }
  .content__title {
    margin: 0;
    font-weight: 700;
    font-size: 55px;
    line-height: 68px;
    white-space: nowrap;
  }
  .content__subtitle {
    margin: 26px 0 0 3px;
    font-weight: 700;
    font-size: 26px;
    line-height: 30px;
  }
  .content__body {
    margin: 12px 0 0 0;
    font-weight: 700;
    font-size: 17px;
    letter-spacing: 0.25px;
    line-height: 34px;
    color: var(--text-soft);
    white-space: nowrap;
  }
  .footer {
    position: absolute;
    left: 0;
    bottom: 0;
    width: 100%;
    height: 57px;
    background: linear-gradient(180deg, #1f1f1f 0%, var(--footer-band) 100%);
  }
  .footer__author {
    position: absolute;
    left: 40px;
    top: 16px;
    font-weight: 700;
    font-size: 19px;
    color: var(--text-light);
  }
</style>
</head>
<body>
  <section class="slide">
    <div class="ribbon">
      <svg class="ribbon__shape" width="206" height="309" viewBox="0 0 206 309" aria-hidden="true">
        <defs>
          <linearGradient id="ribbonFill" x1="0" y1="0" x2="0" y2="1">
            <stop offset="0" stop-color="var(--ribbon-light)"/>
            <stop offset="1" stop-color="var(--ribbon-deep)"/>
          </linearGradient>
        </defs>
        <polygon points="0,0 206,0 206,309 103,257 0,304" fill="url(#ribbonFill)"/>
      </svg>
      <div class="ribbon__url">fjordlineguild.no</div>
      <div class="ribbon__brand">
        <span class="ribbon__square"></span>
        <span class="ribbon__name">Fjordline Data Guild</span>
      </div>
    </div>

    <div class="content">
      <h1 class="content__title">New Product<br>Development 2014</h1>
      <h2 class="content__subtitle">A Brief History</h2>
      <p class="content__body">The FDG is working to improve and renew the special<br>offers to the members in accordance with the different<br>target groups in the member base. We are working hard to<br>promote the Society on the World Wide Web<br>(http://fjordlineguild.no/), and at this time we are inte-<br>grating more functionality for our governing bodies into<br>our Web solution.</p>
    </div>

    <footer class="footer">
      <span class="footer__author">Presentation BY. Ms Maren</span>
    </footer>
  </section>
</body>
</html>
```